Packaging design for aloe lotion bottle for a Laser Clinic

We need a packaging design for a body lotion bottle. Our business is a laser clinic and we are looking at slowly rolling out a range of skincare products. This lotion bottle is the first item with more to follow so the winning designer will have other designs to work on in the future.

The design needs to be classy, elegant, strong and sophisticated. The bottle will be clear with a shiny silver sleeved lid. The lotion itself, which will be visible through the bottle, will be a very light green colour. Think Mirelle Davonne and Voriel as that is the image I want to convey.

Ideally we were thinking of having a design with a single colour but if you come up with a fantastic multi colour design that we love then we're open to it.

Reason: I have extended the deadline as I feel I need more time to allow designers to submit their designs. I haven't found a design that I love just yet. The project has been made a guaranteed payment upon completion. Thank you.

Target Market(s)

upper class high income earners with a high disposable income. People that look after themselves

Industry/Entity Type

Beauty Salon

Colors
000000
cadf82

Requirements
Must have
• must include the details below:
• Post Laser Calming Cream
• This soothing and calming anti inflammatory cream is specifically formulated for use after post laser treatments.
• Fresh Cucumber, Melon and Aloe Vera Leaf Juice blend together in perfect harmony to quickly cool you skin and restore your skins natural moisture.
• Our luxurious calming cream targets redness and helps to reduce inflammation, bringing you supple and radiant skin like never before.
• Directions: Use a liberal amount twice daily on all your treatment areas. This nourishing cream can also be used daily to restore moisture and softness to areas of the face and body not being treated by laser or IPL.
• Ingredients: water (aqua), glycine soja (soybean) oil, cetyl alcohol, glycerin dimethicone, butyrospermum parkii (shea butter), theobroma cacao (cocoa) seed butter, aloe barbadensis (aloe vera) leaf juice, tocopheryl acetate, sodium ascorbyl phosphate, disodium EDTA, ceteareth-20, carbomer, BHT, benzyl benzoate, butylphenyl methylpropional, hexyl cinnamal, linalool, glyceryl caprylate, methylisothiazolinone. May contain: Red 4 (CI 14700, aka 504), Yellow 5 (CI 19140, Ki4), Yellow 6 (CI 15985, KI5), Blue 1 (CI 42090, Ao1), Red 33 (CI 17200, Aka 227), Ext. Violet 2 (CI 60730, Murasaki401), Green 3 (CI 42053, Midori3)
• Against Animal Testing
• Manufactured in Australia
• www.velvetglowclinic.com.au
• 500ml
• Pure Halo Laser Hair Removal logo (see attached files)
Nice to have
• A sophisticated and elegant design
Should not have
• no photos. not too many different colours

```html
<!DOCTYPE html>
<html lang="en">
<head>
<meta charset="utf-8">
<title>Post Laser Calming Cream – Label</title>
<link rel="stylesheet" href="https://fonts.googleapis.com/css2?family=Arimo:wght@700&family=Montserrat:wght@300&family=Pinyon+Script&display=swap">
<style>
  :root {
    --canvas: #e4e4e4;
    --label-black: #000000;
    --label-white: #ffffff;
    --silver-edge: #c9c9c9;
    --silver-mid: #f4f4f4;
    --ink-dark: #111111;
    --aloe-green: #5c9a3a;
    --cucumber: #cadf82;
    --melon: #e9a24f;
  }
  * { margin: 0; padding: 0; box-sizing: border-box; }
  html, body {
    width: 1200px;
    height: 1200px;
    overflow: hidden;
    background: var(--canvas);
  }
  .canvas {
    position: relative;
    width: 1200px;
    height: 1200px;
  }
  .label {
    position: absolute;
    left: 170px;
    top: 147px;
    width: 860px;
    height: 906px;
    background: var(--label-black);
    color: var(--label-white);
  }
  .brand {
    position: absolute;
    top: 70px;
    left: 0;
    width: 100%;
    text-align: center;
    font-family: "Montserrat", sans-serif;
    font-weight: 300;
    color: var(--label-white);
  }
  .brand-name {
    display: block;
    font-size: 78px;
    line-height: 1;
    letter-spacing: 1px;
    text-transform: uppercase;
  }
  .brand-service {
    display: block;
    margin-top: 14px;
    font-size: 27px;
    letter-spacing: 9px;
    text-transform: uppercase;
  }
  .product-band {
    position: absolute;
    top: 321px;
    left: 0;
    width: 100%;
    height: 110px;
    background: linear-gradient(90deg, var(--silver-edge) 0%, var(--silver-mid) 30%, var(--label-white) 50%, var(--silver-mid) 70%, var(--silver-edge) 100%);
    display: flex;
    align-items: center;
    justify-content: center;
  }
  .product-name {
    font-family: "Arimo", sans-serif;
    font-weight: 700;
    font-size: 53px;
    color: var(--ink-dark);
    letter-spacing: -0.5px;
  }
  .tagline {
    position: absolute;
    top: 448px;
    left: 0;
    width: 100%;
    text-align: center;
    font-family: "Pinyon Script", cursive;
    font-size: 62px;
    line-height: 1;
    color: var(--label-white);
  }
  .ingredient-art {
    position: absolute;
    top: 520px;
    left: 306px;
    width: 248px;
    height: 226px;
    border-radius: 50%;
    background: radial-gradient(ellipse at 50% 60%, var(--cucumber) 0%, var(--aloe-green) 45%, rgba(92,154,58,0.25) 75%, rgba(0,0,0,0) 100%);
  }
  .ingredient-art::after {
    content: "";
    position: absolute;
    left: 18px;
    top: 96px;
    width: 70px;
    height: 56px;
    border-radius: 50%;
    background: radial-gradient(circle, var(--melon) 0%, rgba(233,162,79,0) 75%);
  }
  .description {
    position: absolute;
    top: 786px;
    left: 40px;
    right: 40px;
    text-align: center;
    font-family: "Arimo", sans-serif;
    font-weight: 700;
    font-size: 27px;
    line-height: 38px;
    letter-spacing: -0.6px;
    color: var(--label-white);
  }
</style>
</head>
<body>
  <main class="canvas">
    <section class="label">
      <div class="brand">
        <span class="brand-name">Pure Halo</span>
        <span class="brand-service">Laser Hair Removal</span>
      </div>
      <div class="product-band">
        <h1 class="product-name">Post Laser Calming Cream</h1>
      </div>
      <p class="tagline">soothing and calming</p>
      <div class="ingredient-art" role="img" aria-label="Illustration of aloe vera leaves, sliced cucumber and a melon wedge"></div>
      <p class="description">Fresh Cucumber, Melon and Aloe Vera Leaf Juice blend together in perfect harmony to quickly cool you skin and restore your skins natural moisture</p>
    </section>
  </main>
</body>
</html>
```